updated design and flyer

Can you make this into a TRI FOLD design?
We would like the words "Call Bradley" take off and changed to Call us
We would like to add Check out our website at MarbleGateHomeInspectionsTX.com
Please delete the home inspections starting as low at $350.00 and change to " you can now book with us on- line "

```html
<!DOCTYPE html>
<html lang="en">
<head>
<meta charset="utf-8">
<title>Marble Gate Home Inspections – Tri-Fold Brochure</title>
<link href="https://fonts.googleapis.com/css2?family=Montserrat:wght@400;500;700;800&display=swap" rel="stylesheet">
<style>
  :root {
    --red: #b5252d;
    --red-deep: #8e1a20;
    --navy: #1f3d6e;
    --navy-dark: #1a2342;
    --white: #ffffff;
    --paper: #f4f4f4;
    --photo-sky: #9fc0df;
    --photo-tree: #6f9a58;
    --photo-brick: #b49882;
    --ink-blue: #27477d;
  }
  * { margin: 0; padding: 0; box-sizing: border-box; }
  html, body { width: 1200px; height: 900px; overflow: hidden; background: var(--paper); }
  body { font-family: "Montserrat", Arial, sans-serif; }

  .brochure { position: relative; width: 1200px; height: 900px; }
  .brochure-art { position: absolute; inset: 0; }

  .panel { position: absolute; top: 0; width: 400px; height: 900px; }
  .panel--services { left: 0; }
  .panel--contact { left: 400px; }
  .panel--cover { left: 800px; }

  /* Services */
  .service-list { list-style: none; position: absolute; top: 190px; left: 28px; right: 24px; color: var(--white); }
  .service { position: relative; padding-left: 36px; margin-bottom: 40px; }
  .service-star { position: absolute; left: 0; top: 1px; width: 20px; height: 20px; }
  .service-title { font-weight: 800; font-size: 16px; white-space: nowrap; margin-bottom: 8px; }
  .service-text { font-weight: 500; font-size: 14px; line-height: 1.38; }

  /* Contact */
  .contact { position: absolute; top: 270px; left: 20px; right: 20px; text-align: center; color: var(--white); }
  .contact-label { font-weight: 800; font-size: 26px; letter-spacing: 1px; line-height: 1.2; }
  .contact-phone { font-weight: 400; font-size: 40px; line-height: 1.2; margin-bottom: 30px; }
  .contact-item { margin-bottom: 24px; }
  .contact-icon { width: 24px; height: 24px; display: block; margin: 0 auto 6px; }
  .contact-heading { font-weight: 700; font-size: 14px; line-height: 1.2; margin-bottom: 3px; }
  .contact-detail { font-weight: 500; font-size: 13.5px; line-height: 1.25; }
  .contact-web { font-weight: 500; font-size: 13.5px; line-height: 1.3; }
  .contact-web-url { display: block; font-weight: 700; }
  .contact-booking { font-weight: 700; font-size: 13.5px; margin-top: 8px; }

  /* Cover */
  .brand { position: absolute; top: 428px; left: 40px; display: flex; align-items: center; gap: 10px; }
  .brand-dot { width: 16px; height: 16px; border-radius: 50%; background: var(--navy); }
  .brand-name { font-weight: 500; font-size: 15px; color: var(--navy); letter-spacing: .5px; }
  .headline { position: absolute; top: 510px; left: 40px; font-size: 32px; line-height: 1.12; }
  .headline-lead { display: block; font-weight: 400; color: var(--ink-blue); }
  .headline-key { display: block; font-weight: 800; color: var(--ink-blue); }
  .headline-place { display: block; font-weight: 400; color: var(--red); white-space: nowrap; }
</style>
</head>
<body>
<main class="brochure">
  <svg class="brochure-art" width="1200" height="900" viewBox="0 0 1200 900">
    <defs>
      <linearGradient id="navyFill" x1="0" y1="0" x2="1" y2="1">
        <stop offset="0" stop-color="#3a5f94"/>
        <stop offset="1" stop-color="#1d3a68"/>
      </linearGradient>
      <linearGradient id="topPhoto" x1="0" y1="0" x2="0" y2="1">
        <stop offset="0" stop-color="var(--photo-sky)"/>
        <stop offset=".45" stop-color="var(--photo-tree)"/>
        <stop offset="1" stop-color="var(--photo-brick)"/>
      </linearGradient>
      <linearGradient id="bottomPhoto" x1="0" y1="0" x2="0" y2="1">
        <stop offset="0" stop-color="var(--photo-sky)"/>
        <stop offset=".4" stop-color="var(--photo-brick)"/>
        <stop offset="1" stop-color="#8d7a68"/>
      </linearGradient>
    </defs>

    <rect class="bg-services" x="0" y="0" width="400" height="900" fill="var(--red)"/>
    <rect class="bg-contact" x="400" y="0" width="400" height="900" fill="url(#navyFill)"/>
    <rect class="bg-cover" x="800" y="0" width="400" height="900" fill="var(--white)"/>

    <!-- top photograph band -->
    <path class="accent-navy" d="M400 40 L700 200 Q735 222 720 255 L400 85 Z" fill="var(--navy-dark)"/>
    <path d="M440 0 H1200 V300 L1110 375 Q1085 395 1055 383 L800 268 L720 228 L440 40 Z"
          fill="url(#topPhoto)" role="img" aria-label="Photo of a two-storey brick house behind tall trees"/>

    <!-- cover red corners -->
    <path class="accent-red" d="M1200 240 V410 L1120 345 Q1102 325 1125 305 Z" fill="var(--red)"/>
    <path class="accent-red" d="M1200 640 V800 L1125 815 Q1140 700 1200 640 Z" fill="var(--red)"/>

    <!-- bottom photograph -->
    <path class="accent-red-deep" d="M250 705 Q285 670 330 682 L400 705 L400 760 Z" fill="var(--red-deep)"/>
    <path class="accent-navy" d="M400 780 L545 900 H505 L400 812 Z" fill="var(--navy-dark)"/>
    <path d="M0 840 L150 705 Q180 680 215 692 L400 790 L520 900 H0 Z"
          fill="url(#bottomPhoto)" role="img" aria-label="Photo of a brick family home with garage and landscaped front yard"/>
  </svg>

  <section class="panel panel--services">
    <ul class="service-list">
      <li class="service">
        <svg class="service-star" viewBox="0 0 24 24"><polygon points="12,1 15,9 23,9 16.5,14 19,22 12,17 5,22 7.5,14 1,9 9,9" fill="#fff"/></svg>
        <h3 class="service-title">Pre-Purchase Home Inspection</h3>
        <p class="service-text">Ensure that the home you are considering meets your expectations and identify any potential issues before making a purchase.</p>
      </li>
      <li class="service">
        <svg class="service-star" viewBox="0 0 24 24"><polygon points="12,1 15,9 23,9 16.5,14 19,22 12,17 5,22 7.5,14 1,9 9,9" fill="#fff"/></svg>
        <h3 class="service-title">Pre-Listing Home Inspection</h3>
        <p class="service-text">Get a thorough evaluation of your property's condition before listing it for sale, allowing you to address any necessary repairs beforehand.</p>
      </li>
      <li class="service">
        <svg class="service-star" viewBox="0 0 24 24"><polygon points="12,1 15,9 23,9 16.5,14 19,22 12,17 5,22 7.5,14 1,9 9,9" fill="#fff"/></svg>
        <h3 class="service-title">New Construction Inspection</h3>
        <p class="service-text">Verify the quality and craftsmanship of your newly built home, ensuring it meets industry standards and your expectations.</p>
      </li>
    </ul>
  </section>

  <section class="panel panel--contact">
    <div class="contact">
      <h2 class="contact-label">CALL US</h2>
      <p class="contact-phone">(281) 555-0142</p>
      <div class="contact-item">
        <svg class="contact-icon" viewBox="0 0 24 24"><circle cx="12" cy="12" r="10" fill="none" stroke="#fff" stroke-width="2"/><path d="M12 6v6l4 2" fill="none" stroke="#fff" stroke-width="2"/></svg>
        <p class="contact-heading">Business Hours</p>
        <p class="contact-detail">Monday - Sunday 9AM - 6PM</p>
      </div>
      <div class="contact-item">
        <svg class="contact-icon" viewBox="0 0 24 24"><rect x="2" y="5" width="20" height="14" fill="#fff"/><path d="M2 5l10 8 10-8" fill="none" stroke="#1f3d6e" stroke-width="1.6"/></svg>
        <p class="contact-heading">Email</p>
        <p class="contact-detail">Marblegatehomeinspectionstx@gmail.com</p>
      </div>
      <div class="contact-item">
        <svg class="contact-icon" viewBox="0 0 24 24"><path d="M12 2a7 7 0 0 0-7 7c0 5 7 13 7 13s7-8 7-13a7 7 0 0 0-7-7z" fill="none" stroke="#fff" stroke-width="2"/><circle cx="12" cy="9" r="2.5" fill="#fff"/></svg>
        <p class="contact-heading">Service Area</p>
        <p class="contact-detail">Serving The Woodlands &amp; Surrounding Areas</p>
      </div>
      <p class="contact-web">Check out our website at <span class="contact-web-url">MarbleGateHomeInspectionsTX.com</span></p>
      <p class="contact-booking">You can now book with us online</p>
    </div>
  </section>

  <section class="panel panel--cover">
    <div class="brand">
      <span class="brand-dot"></span>
      <span class="brand-name">MARBLE GATE HOME INSPECTIONS</span>
    </div>
    <h1 class="headline">
      <span class="headline-lead">Professional</span>
      <span class="headline-key">Home</span>
      <span class="headline-key">Inspections</span>
      <span class="headline-place">in The Woodlands</span>
    </h1>
  </section>
</main>
</body>
</html>
```